Book cover: Stormy Days Survival for Kids (A5)

I have a book called Stormy Days Survival for Teens. It is a book for teenagers which gives them tips and tactics on how to survive life's challenges regarding friends, family, feelings, relationships and hard stuff in life generally. I will upload the cover of this book but you can see it on my past jobs as one of the designers her eon Pixel Bazaar did it for me.
I have a new book I've written called Stormy Days Survival for Kids. This is a parallel book to Stormy Days Survival for Teens, but it is specifically for 8 to 12 or 13 year olds, rather than for older teens.
A very important aspect of this job is that it SHOULD MATCH in some strong way - the Stormy Days Survival for Teens book. I will be selling them together, displaying them together and I want them to look like two of a pair. It might be that you use the same image as the first book but change the colour of the image so that it is bright orange and green perhaps? Or that there is another image but in the image is placed in the exact same position across the book as the first book. It needs to look like the books are by the same author.
However, I would like this one to look a bit "younger", more kid friendly. For example, a font that looks like it is for kids, or kids' writing perhaps.
I dont want to have photos on the book, and I dont think I want cartoons or drawings - because I'm not sure how this will tie in with the first book.
I want it to look modern, fresh and designed specifically for kids. The text needs to be:
Stormy Days Survival - For Kids!
Tips and ideas for 8 to 13 year olds about how to stay cool, calm and confident on even the toughest days!
The back cover is going to mostly just have the table of contents listed and a blurb, with one or two cartoons which I will supply. I am keen to pick a designer to just do the front cover first and will ask them to do the back cover later.
UPDATED: I have attached three files with fonts that I like.

```html
<!DOCTYPE html>
<html lang="en">
<head>
<meta charset="utf-8">
<title>Stormy Days Survival for Kids – Cover</title>
<link rel="stylesheet" href="https://fonts.googleapis.com/css2?family=Gloria+Hallelujah&family=Arimo:wght@400;700&display=swap">
<style>
  :root {
    --paper: #ffffff;
    --ink: #111111;
    --sun-light: #ffe24a;
    --sun-mid: #fcd022;
    --sun-deep: #f6b417;
  }
  html, body {
    margin: 0;
    padding: 0;
    overflow: hidden;
    background: var(--paper);
  }
  .cover {
    position: relative;
    width: 846px;
    height: 1200px;
    background: var(--paper);
    overflow: hidden;
    color: var(--ink);
  }
  .title {
    position: absolute;
    left: 82px;
    top: 84px;
    margin: 0;
    font-family: "Gloria Hallelujah", cursive;
    font-weight: 400;
    line-height: 1;
    text-transform: uppercase;
  }
  .title span { display: block; }
  .title-lead {
    font-size: 60px;
    letter-spacing: 1px;
  }
  .title-main {
    font-size: 100px;
    margin-top: -10px;
    letter-spacing: 2px;
  }
  .title-tail {
    font-size: 80px;
    margin-top: -8px;
  }
  .star-band {
    position: absolute;
    left: 0;
    top: 386px;
    width: 846px;
    height: 533px;
    background: radial-gradient(ellipse at 40% 45%, var(--sun-light) 0%, var(--sun-mid) 55%, var(--sun-deep) 100%);
  }
  .tagline {
    position: absolute;
    left: 123px;
    top: 600px;
    width: 600px;
    margin: 0;
    font-family: "Arimo", sans-serif;
    font-weight: 700;
    font-size: 30px;
    line-height: 1.35;
    text-align: center;
    color: var(--ink);
  }
  .credits {
    position: absolute;
    left: 414px;
    top: 1026px;
    width: 420px;
    text-align: center;
  }
  .author {
    margin: 0;
    font-family: "Gloria Hallelujah", cursive;
    font-size: 40px;
    line-height: 1.2;
    text-transform: uppercase;
    letter-spacing: 1px;
    white-space: nowrap;
  }
  .author-role {
    margin: 8px 0 0;
    font-family: "Arimo", sans-serif;
    font-size: 24px;
    line-height: 1.1;
  }
  .illustrator {
    margin: 10px 0 0;
    font-family: "Arimo", sans-serif;
    font-size: 16px;
    line-height: 1.1;
  }
</style>
</head>
<body>
  <main class="cover">
    <h1 class="title">
      <span class="title-lead">Stormy Days</span>
      <span class="title-main">Survival</span>
      <span class="title-tail">For Kids!</span>
    </h1>

    <div class="star-band" role="img" aria-label="Crowd of smiling yellow cartoon stars with one sad blue star among them"></div>

    <p class="tagline">Tips and ideas for 8 to 13 year olds about how to stay cool, calm and confident on even the toughest days!</p>

    <div class="credits">
      <p class="author">Maren Holloway</p>
      <p class="author-role">clinical psychologist</p>
      <p class="illustrator">Illustrated by: Tessa Rowe</p>
    </div>
  </main>
</body>
</html>
```